Business Card Design Project

I help solve problems that people have with real estate, so I buy homes for cash that they no longer want, can't afford, inherited, etc. and fix and sell them or rent them or take over mortgage payments. See website: www.quickdeedhomestead.com

Industry/Entity Type

Real Estate

Contact Information for Business Card

Not exactly sure. Looking for a design that either is similar to the website www.quickdeedhomestead.com or that reflects what I do as described below. If it can look a little luxurious to show I can buy the houses for cash and I fix them and sell them, it's a bonus. I seem to like some of the higher end things like foil or black or something that makes it stand out.

Font styles to use
Serif

Requirements
Nice to have
• I seem to like black or clear. I like things to stand out and be different.

```html
<!DOCTYPE html>
<html lang="en">
<head>
<meta charset="utf-8">
<title>Harborline Homes – Business Card</title>
<link href="https://fonts.googleapis.com/css2?family=Questrial&display=swap" rel="stylesheet">
<style>
  :root {
    --bg: #e9e7e3;
    --card-black: #0b0b0b;
    --card-black-soft: #1e1e1e;
    --card-white: #ffffff;
    --ink: #1a1a1a;
    --green: #4cae3a;
    --green-light: #7cd05d;
    --text-light: #f2f2f2;
    --text-muted: #c9c9c9;
    --divider: #8a8a8a;
  }
  * { box-sizing: border-box; margin: 0; padding: 0; }
  html, body { width: 1200px; height: 800px; overflow: hidden; }
  body {
    background: var(--bg);
    font-family: "Questrial", "Century Gothic", sans-serif;
    position: relative;
  }
  .card {
    position: absolute;
    width: 525px;
    height: 300px;
    border-radius: 4px;
    overflow: hidden;
    box-shadow: 0 10px 30px rgba(0,0,0,.25);
  }
  .brand-name {
    text-transform: uppercase;
    white-space: nowrap;
    letter-spacing: 2px;
    line-height: 1;
  }
  /* Back side */
  .card-back {
    left: 50px;
    top: 250px;
    background: radial-gradient(ellipse at 50% 45%, var(--card-black-soft) 0%, var(--card-black) 70%);
    display: flex;
    align-items: center;
    justify-content: center;
  }
  .card-back .brand-name { color: var(--text-light); font-size: 40px; }
  /* Front side */
  .card-front {
    left: 625px;
    top: 250px;
    background: var(--card-white);
  }
  .card-front .waves { position: absolute; inset: 0; width: 100%; height: 100%; }
  .card-front .brand-name {
    position: absolute;
    left: 28px;
    top: 52px;
    font-size: 38px;
    color: var(--ink);
  }
  .holder {
    position: absolute;
    left: 30px;
    top: 205px;
    width: 210px;
    text-align: right;
  }
  .holder-name { color: var(--green-light); font-size: 17px; }
  .holder-title { color: var(--text-muted); font-size: 12px; margin-top: 4px; }
  .divider {
    position: absolute;
    left: 258px;
    top: 195px;
    width: 1px;
    height: 85px;
    background: var(--divider);
  }
  .contact-list {
    position: absolute;
    left: 272px;
    top: 197px;
    list-style: none;
    color: var(--text-light);
    font-size: 11.5px;
  }
  .contact-list li { display: flex; align-items: flex-start; gap: 7px; line-height: 17px; }
  .contact-list svg { width: 12px; height: 12px; margin-top: 2px; flex: none; fill: var(--green-light); }
  .contact-list .address-line { padding-left: 19px; }
</style>
</head>
<body>

<section class="card card-back" aria-label="Card back">
  <div class="brand-name">Harborline Homes</div>
</section>

<section class="card card-front" aria-label="Card front">
  <svg class="waves" viewBox="0 0 525 300" preserveAspectRatio="none" aria-hidden="true">
    <defs>
      <linearGradient id="darkBand" x1="0" y1="0" x2="0" y2="1">
        <stop offset="0" stop-color="#2a2a2a"/>
        <stop offset="1" stop-color="#050505"/>
      </linearGradient>
    </defs>
    <path d="M180 170 C300 160 430 150 525 95 L525 125 C430 165 320 172 180 170 Z" fill="var(--green)"/>
    <path d="M0 205 C40 175 120 165 230 168 C360 170 460 150 525 118 L525 300 L0 300 Z" fill="url(#darkBand)"/>
  </svg>

  <div class="brand-name">Harborline Homes</div>

  <div class="holder">
    <div class="holder-name">Marcus Whitfield</div>
    <div class="holder-title">Manager</div>
  </div>
  <div class="divider"></div>

  <ul class="contact-list">
    <li><svg viewBox="0 0 24 24"><path d="M6.6 10.8a15 15 0 0 0 6.6 6.6l2.2-2.2c.3-.3.7-.4 1-.2 1.1.4 2.3.6 3.6.6.6 0 1 .4 1 1V20c0 .6-.4 1-1 1C10.6 21 3 13.4 3 4c0-.6.4-1 1-1h3.5c.6 0 1 .4 1 1 0 1.3.2 2.5.6 3.6.1.3 0 .7-.2 1z"/></svg>(402) 555-0147</li>
    <li><svg viewBox="0 0 24 24"><path d="M2 5h20v14H2z M2 5l10 8 10-8" fill="none" stroke="var(--green-light)" stroke-width="2.2"/></svg>marcus@quickdeedhomestead.com</li>
    <li><svg viewBox="0 0 24 24"><circle cx="12" cy="12" r="9" fill="none" stroke="var(--green-light)" stroke-width="2"/><path d="M3 12h18M12 3c3 3 3 15 0 18M12 3c-3 3-3 15 0 18" fill="none" stroke="var(--green-light)" stroke-width="1.6"/></svg>www.quickdeedhomestead.com</li>
    <li><svg viewBox="0 0 24 24"><path d="M12 3 2 12h3v9h5v-6h4v6h5v-9h3z"/></svg>4820 North Elm Avenue, Ste 210</li>
    <li class="address-line">Philadelphia Pa.</li>
  </ul>
</section>

</body>
</html>
```